IT services company needs a business card designed

-2 sided business card.-Front is going to be the logo raised (3D floating effect) on a black background. Make the logos spider web shiny silver and keep the spider the same design. -Back needs to have the following information:Darrel Sotho, Managing Partner, Cell: 738-402-1954, Website: Plankhorn.com, Email: Darrel@Plankhorn.com
Target Market(s)
IT Services
Industry/Entity Type
It Company
Contact Information for Business Card
-2 sided business card.
-Front is going to be the logo raised (3D floating effect) on a black background. Make the logos spider web shiny silver and keep the spider the same design.
-Back needs to have the following information:
Darrel Sotho, Managing Partner, Cell: 738-402-1954, Website: Plankhorn.com, Email: Darrel@Plankhorn.com

```html
<!DOCTYPE html>
<html lang="en">
<head>
<meta charset="utf-8">
<title>Plankhorn Business Card</title>
<link rel="stylesheet" href="https://fonts.googleapis.com/css2?family=Oswald:wght@500&family=Ropa+Sans&display=swap">
<style>
  :root {
    --stage-bg: #2c2c2e;
    --card-front: #ffffff;
    --card-back: #3a393b;
    --brand-blue: #1a7fc1;
    --ink: #1c1c1e;
    --wordmark: #262527;
  }
  * { margin: 0; padding: 0; box-sizing: border-box; }
  html, body {
    width: 1200px; height: 1200px; overflow: hidden;
    background: var(--stage-bg);
  }
  .stage { position: relative; width: 1200px; height: 1200px; }
  .card {
    position: absolute; left: 193px; width: 880px; height: 502px;
    border-radius: 36px; overflow: hidden;
  }
  .card--front { top: 34px; background: var(--card-front); }
  .card--back { top: 664px; background: var(--card-back); }

  .identity {
    position: absolute; right: 489px; top: 210px; text-align: right;
  }
  .identity__name {
    font-family: "Oswald", sans-serif; font-weight: 500;
    font-size: 46px; line-height: 52px; color: var(--brand-blue);
    text-transform: uppercase; letter-spacing: -0.5px; white-space: nowrap;
  }
  .identity__title {
    font-family: "Ropa Sans", sans-serif; font-size: 21px;
    line-height: 24px; color: var(--ink);
  }
  .divider {
    position: absolute; left: 435px; top: 212px; width: 4px; height: 77px;
    background: var(--brand-blue);
  }
  .contact { position: absolute; left: 488px; top: 208px; list-style: none; }
  .contact__row {
    display: flex; align-items: center; height: 28px;
    font-family: "Ropa Sans", sans-serif; font-size: 20px; color: var(--ink);
  }
  .contact__icon { width: 18px; height: 18px; margin-right: 20px; flex: none; }
  .contact__icon * { fill: none; stroke: var(--brand-blue); stroke-width: 1.6; }
  .contact__icon .solid { fill: var(--brand-blue); stroke: none; }

  .brand {
    position: absolute; left: 0; right: 0; top: 342px; text-align: center;
    font-family: "Ropa Sans", sans-serif; font-size: 66px; line-height: 72px;
    letter-spacing: 4px; color: var(--wordmark); text-transform: uppercase;
  }
  .brand__dot {
    position: absolute; left: 434px; top: 424px; width: 13px; height: 13px;
    border-radius: 50%; background: var(--brand-blue);
  }
</style>
</head>
<body>
<main class="stage">
  <section class="card card--front">
    <div class="identity">
      <h1 class="identity__name">Darrel Sotho</h1>
      <p class="identity__title">Managing Partner</p>
    </div>
    <div class="divider"></div>
    <ul class="contact">
      <li class="contact__row">
        <svg class="contact__icon" viewBox="0 0 24 24"><path class="solid" d="M6.6 10.8c1.4 2.8 3.8 5.2 6.6 6.6l2.2-2.2c.3-.3.7-.4 1-.2 1.1.4 2.3.6 3.6.6.6 0 1 .4 1 1V20c0 .6-.4 1-1 1C10.6 21 3 13.4 3 4c0-.6.4-1 1-1h3.5c.6 0 1 .4 1 1 0 1.2.2 2.4.6 3.6.1.3 0 .7-.2 1z"/></svg>
        <span>738-402-1954</span>
      </li>
      <li class="contact__row">
        <svg class="contact__icon" viewBox="0 0 24 24"><rect x="2" y="5" width="20" height="14"/><path d="M2 5l10 8 10-8M2 19l7-7M22 19l-7-7"/></svg>
        <span>Darrel@Plankhorn.com</span>
      </li>
      <li class="contact__row">
        <svg class="contact__icon" viewBox="0 0 24 24"><circle cx="12" cy="12" r="9.5"/><ellipse cx="12" cy="12" rx="4.5" ry="9.5"/><path d="M2.5 12h19M4 7h16M4 17h16"/></svg>
        <span>www.plankhorn.com</span>
      </li>
    </ul>
  </section>

  <section class="card card--back">
    <p class="brand">Plankhorn</p>
    <span class="brand__dot"></span>
  </section>
</main>
</body>
</html>
```